Actors Postcard Design

I need a postcard designed for me. I am an actor, voice over artist and technical adviser for tv, film and videogames. I am open to color ideas. My photos are in black and white so something to make those stand out a bit. Masculine colors like dark blue etc..I have seen some of your designs with 3 photos which I liked. Perhaps a 2-3 photo scheme. Back of postcard to contain my resume. Want it to look professional and not cartoonish (since I mentioned video games). Front to have photos and job title and contact info

Please take my color direction lightly, I am open to all color schemes. light or dark. You are the professionals. Am looking forward to seeing what all of you come up with. Thanks

Tv

```html
<!DOCTYPE html>
<html lang="en">
<head>
<meta charset="utf-8">
<title>Tomasz Kowalczyk – Actor Postcard</title>
<link rel="stylesheet" href="https://fonts.googleapis.com/css2?family=Montserrat:wght@400;600;700&family=Questrial&display=swap">
<style>
  :root {
    --page: #ffffff;
    --card: #ffffff;
    --ink: #2e2e2e;
    --panel: #4a4a4a;
    --rule: #d6d6d6;
    --photo-dark: #3b3b3b;
    --photo-mid: #8a8a8a;
    --photo-light: #c9c9c9;
    --white: #ffffff;
  }
  * { box-sizing: border-box; margin: 0; padding: 0; }
  html, body { width: 809px; height: 1200px; overflow: hidden; background: var(--page); }
  body { position: relative; font-family: "Questrial", sans-serif; color: var(--ink); }

  .card { position: absolute; left: 28px; width: 752px; background: var(--card); box-shadow: 0 2px 8px rgba(0,0,0,.18); }

  /* Front */
  .card-front { top: 10px; height: 580px; }
  .front-photo { position: absolute; inset: 14px; background: radial-gradient(ellipse at 68% 40%, var(--photo-light) 0%, var(--photo-mid) 38%, var(--photo-dark) 100%); }
  .front-title { position: absolute; left: 80px; top: 272px; color: var(--white); }
  .front-name { font-family: "Montserrat", sans-serif; font-weight: 700; font-size: 27px; line-height: 1.15; letter-spacing: .5px; }
  .front-name .nick { font-weight: 400; }
  .front-roles { font-family: "Montserrat", sans-serif; font-weight: 600; font-size: 11px; margin-top: 8px; }

  /* Back */
  .card-back { top: 616px; height: 574px; }
  .back-name { position: absolute; right: 30px; top: 30px; font-family: "Montserrat", sans-serif; font-size: 19px; font-weight: 700; letter-spacing: .5px; }
  .back-name .nick { font-weight: 400; }
  .photo-row { position: absolute; top: 76px; left: 0; right: 0; height: 186px; display: flex; gap: 9px; }
  .headshot { flex: 0 0 241px; background: radial-gradient(ellipse at 50% 40%, var(--photo-light) 0%, var(--photo-mid) 45%, var(--photo-dark) 100%); }
  .headshot-alt { flex: 0 0 250px; background: radial-gradient(ellipse at 50% 45%, var(--photo-light) 0%, var(--photo-mid) 40%, #4f4f4f 100%); }
  .role-panel { flex: 1; background: var(--panel); color: var(--white); padding: 22px 10px 0 30px; font-family: "Montserrat", sans-serif; font-size: 20px; line-height: 1.2; list-style: none; }
  .role-panel .cont { padding-left: 16px; display: inline-block; }

  .specs { position: absolute; top: 290px; left: 36px; right: 30px; display: flex; gap: 22px; font-size: 11px; align-items: baseline; padding-bottom: 10px; border-bottom: 1px solid var(--rule); }
  .specs b { font-family: "Montserrat", sans-serif; font-weight: 700; }
  .specs .contact { margin-left: 26px; }

  .column { position: absolute; top: 338px; width: 320px; font-size: 11px; line-height: 1.4; }
  .col-left { left: 36px; }
  .col-right { left: 398px; }
  .divider { position: absolute; top: 338px; left: 376px; width: 1px; height: 210px; background: var(--rule); }
  .col-heading { font-family: "Montserrat", sans-serif; font-weight: 700; font-size: 18px; line-height: 1.1; }
  .col-sub { font-style: italic; font-weight: 600; font-size: 11.5px; margin-bottom: 22px; }
  .block-title { font-family: "Montserrat", sans-serif; font-weight: 700; font-size: 11.5px; }
  .block { margin-bottom: 16px; }
</style>
</head>
<body>

<section class="card card-front">
  <div class="front-photo" role="img" aria-label="Black and white portrait of the actor outdoors, wearing a dark jacket"></div>
  <div class="front-title">
    <h1 class="front-name">TOMASZ<br><span class="nick">“TOM” KOWALCZYK</span></h1>
    <p class="front-roles">Actor, Voice over Artist, Technical Advisor</p>
  </div>
</section>

<section class="card card-back">
  <h2 class="back-name">TOMASZ <span class="nick">“TOM”</span> KOWALCZYK</h2>
  <div class="photo-row">
    <div class="headshot" role="img" aria-label="Black and white headshot of the actor in a dark shirt"></div>
    <div class="headshot-alt" role="img" aria-label="Headshot of the actor in a plaid shirt outdoors"></div>
    <ul class="role-panel">
      <li>- ACTOR</li>
      <li>- VOICE OVER<br><span class="cont">ARTIST</span></li>
      <li>- TECHNICAL<br><span class="cont">ADVISOR</span></li>
    </ul>
  </div>

  <div class="specs">
    <span><b>Height:</b> 6’0”</span>
    <span><b>Weight:</b> 180</span>
    <span><b>Hair:</b> Blond</span>
    <span><b>Eyes:</b> Green</span>
    <span class="contact"><b>tomkowalczyk@mailbox.test</b></span>
    <span>555-014-2290</span>
  </div>

  <div class="column col-left">
    <h3 class="col-heading">Training/Experience</h3>
    <p class="col-sub">Acting</p>
    <div class="block">
      <p>Mara Ellison Acting School – 1.5 yrs</p>
      <p>Actors Workshop Northwest – On Camera 2yrs</p>
      <p>HCS Highland Coach Studio – 5 day intensive</p>
    </div>
    <div class="block">
      <p class="block-title">Voice Over</p>
      <p>Voice Forge – Dayline Conservatory<br>(commercial, narration, etc…)</p>
    </div>
    <p>- Adv Dayline Conservatory<br>- 4 day Character Intensive</p>
  </div>

  <div class="divider"></div>

  <div class="column col-right">
    <h3 class="col-heading">Technical Advising</h3>
    <p class="col-sub">FNA Special Agent – 10.5 yrs</p>
    <div class="block">
      <p><b>Extensive Firearms Training</b> – FNA, Norse Tactics, Former Granite Unit Members, Ridge Team Seven. Defensive Tactics, Breaching, Vehicle Containment, Surveillance, etc….</p>
    </div>
    <div class="block">
      <p class="block-title">Special Skills</p>
      <p>15 yrs martial arts (Gung Fu, Judo, Tai Chi, Kenjutsu), EMT, Personal Trainer, Scuba, Snowboarding, Snowshoeing, Alpine Mountaineering, Archery, Mountainbiking, SUP, Blacksmithing, Carpentry 7yrs, Fluent Polish.</p>
    </div>
  </div>
</section>

</body>
</html>
```